Business Card (double-sided) and Stationary Design for dental office

1) Business Card Design: We need a business card design for a dental specialty office.
Texts should contain:
The name of our office "Bayhaven Grins Orthodontics"
Tagline: "Specialist in Orthodontic and Maxillofacial Orthopedics"
Tag line: "Creating "Talvering" smiles for Children and Adults"
Doctor name: "Doctor Name"
Office Address:
"123 Street Name
City, State Zip code"
Office email address: office@bayhavengrins.com
Website: www.bayhavengrins.com

We will provide the full office address once the design is selected
Theme: beach, paradise, coastal, wave
We would like to have some creativity in design. Some acceptable ideas: front page: logo and office name. Back page: more detail information, and map to office in form of an island. Please see sample from our other location, but you DON'T HAVE TO USE OR COPY THE SAME CONCEPT.

IF POSSIBLE, PLEASE SUBMIT AT LEAST TWO CONCEPTS: ONE WITH THE BACK LOOKING SIMILAR TO WHAT IS IN THE SAMPLE, AND ONE DIFFERENT.

Color: designer to choose. We have different shade of blues and sand color in our office. Please see logo.

2) Please also design a matching set of stationary that compliment the business card and our logo.

Target Market(s)

Dental

Contact Information for Business Card

See descriptions

Font styles to use
Other font styles liked:
• Matching texts in logo

Colors
0054AA
0677BA
7BADD7
CADEEF
E8F1F8
0094D4
00A9DD
6FCCEA
C7EBF8
E9F6FB
00AB8E
00BBA5
67D7C9
C6EFE9
E9F9F6

Requirements
Must have
• Double-sided
Nice to have
• Beach coastal theme
Should not have
• Any shape or drawing of of tooth or teeth. We don’t need these. You don't necessarily have to just cut and paste the logo art and text as a whole, you have the liberty to rearrange the text.

```html
<!DOCTYPE html>
<html lang="en">
<head>
<meta charset="utf-8">
<title>Bayhaven Grins Orthodontics — Business Card</title>
<link href="https://fonts.googleapis.com/css2?family=Montserrat:wght@600;700;800&family=Roboto:ital,wght@0,400;0,500;0,700;1,700&display=swap" rel="stylesheet">
<style>
  :root {
    --page-bg: #d9d9dc;
    --card-white: #ffffff;
    --teal: #2a87a5;
    --teal-deep: #1f6f8c;
    --mint: #6fcbb9;
    --navy: #1d5a86;
    --sand-light: #fbe3b0;
    --sand: #f4c374;
    --sand-deep: #eea245;
    --sea: #19a3dc;
    --text-light: #ffffff;
    --text-muted: #5d8fb0;
  }
  * { box-sizing: border-box; margin: 0; padding: 0; }
  html, body {
    width: 1200px; height: 800px; overflow: hidden;
    background: var(--page-bg);
    font-family: "Roboto", Arial, sans-serif;
  }
  .sheet {
    position: relative; width: 1200px; height: 800px;
    display: flex; flex-direction: column; align-items: center;
    justify-content: center; gap: 28px;
  }
  .card {
    position: relative; width: 640px; height: 366px;
    border-radius: 24px; overflow: hidden;
    background: var(--card-white);
    box-shadow: 0 6px 18px rgba(0,0,0,0.18);
  }

  /* ---------- front ---------- */
  .front-wave { position: absolute; inset: 0; }
  .brand {
    position: absolute; left: 50px; top: 60px;
    display: flex; align-items: center; gap: 14px;
  }
  .brand-dot {
    width: 58px; height: 58px; border-radius: 50%;
    background: var(--teal); flex: none;
  }
  .brand-name {
    font-family: "Montserrat", Arial, sans-serif;
    font-weight: 700; font-size: 34px; color: var(--teal-deep);
    line-height: 1; white-space: nowrap;
  }
  .brand-sub {
    font-family: "Montserrat", Arial, sans-serif;
    font-weight: 600; font-size: 11px; letter-spacing: 1.2px;
    color: var(--mint); margin-top: 6px; white-space: nowrap;
  }
  .office-address {
    position: absolute; right: 34px; top: 150px;
    text-align: right; color: var(--text-light);
    font-size: 15px; line-height: 1.35; font-style: normal;
  }
  .contact {
    position: absolute; left: 34px; top: 262px; color: var(--text-light);
  }
  .contact-name {
    font-weight: 700; font-size: 22px; letter-spacing: 1px;
    margin-bottom: 4px; line-height: 1.1;
  }
  .contact-line {
    display: flex; align-items: center; gap: 8px;
    font-size: 14px; line-height: 1.3;
  }
  .contact-line svg { width: 12px; height: 12px; flex: none; }
  .front-tagline {
    position: absolute; left: 300px; top: 330px;
    color: var(--text-light); font-weight: 700; font-style: italic;
    font-size: 14px; white-space: nowrap;
  }

  /* ---------- back ---------- */
  .appointment-title {
    position: absolute; left: 36px; top: 28px;
    font-family: "Montserrat", Arial, sans-serif;
    font-weight: 800; font-size: 25px; color: var(--navy);
    letter-spacing: 0.3px;
  }
  .field {
    position: absolute; display: flex; align-items: flex-end;
    color: var(--text-muted); font-size: 15px;
  }
  .field-line {
    flex: 1; border-bottom: 1.5px dotted var(--text-muted);
    margin-left: 4px; margin-bottom: 4px;
  }
  .field-for { left: 36px; top: 78px; width: 570px; }
  .field-date { left: 36px; top: 114px; width: 300px; }
  .field-time { left: 350px; top: 114px; width: 256px; }
  .scene-art {
    position: absolute; left: 0; right: 0; top: 196px; bottom: 0;
    background:
      linear-gradient(180deg, rgba(255,255,255,0.9) 0%, rgba(255,255,255,0) 30%),
      linear-gradient(100deg, var(--sand-light) 0%, var(--sand) 45%, var(--sand-deep) 100%);
  }
  .scene-art::after {
    content: ""; position: absolute; left: 0; right: 0; bottom: 0; height: 22px;
    background: var(--sea);
  }
  .specialty-band {
    position: absolute; left: 140px; right: -20px; top: 168px; height: 30px;
    background: var(--teal); border-radius: 15px 0 0 15px;
    color: var(--text-light); font-weight: 700; font-size: 15px;
    display: flex; align-items: center; padding-left: 22px;
  }
</style>
</head>
<body>
<main class="sheet">

  <!-- Front side -->
  <section class="card card-front" aria-label="Business card front">
    <svg class="front-wave" viewBox="0 0 640 366" aria-hidden="true">
      <path d="M0,248 Q420,222 560,0 L640,0 L640,366 L0,366 Z" fill="var(--teal)"/>
      <path d="M0,238 Q408,210 546,0" fill="none" stroke="var(--mint)" stroke-width="3"/>
    </svg>

    <div class="brand">
      <span class="brand-dot"></span>
      <div>
        <div class="brand-name">Bayhaven Grins</div>
        <div class="brand-sub">Pediatric Dentistry &amp; Orthodontics</div>
      </div>
    </div>

    <address class="office-address">
      Bayhaven Grins Dentistry<br>
      123 Street Name<br>
      City, State Zip code
    </address>

    <div class="contact">
      <div class="contact-name">DANIEL HARROW</div>
      <div class="contact-line">
        <svg viewBox="0 0 24 24"><path fill="#fff" d="M6.6 10.8a15 15 0 0 0 6.6 6.6l2.2-2.2a1 1 0 0 1 1-.25 11.4 11.4 0 0 0 3.6.57 1 1 0 0 1 1 1V20a1 1 0 0 1-1 1A17 17 0 0 1 3 4a1 1 0 0 1 1-1h3.5a1 1 0 0 1 1 1c0 1.25.2 2.45.57 3.57a1 1 0 0 1-.25 1z"/></svg>
        555-014-2290
      </div>
      <div class="contact-line">
        <svg viewBox="0 0 24 24"><path fill="#fff" d="M2 5h20v14H2z M2 5l10 8 10-8" stroke="#2a87a5" stroke-width="1.5"/></svg>
        office@bayhavengrins.com
      </div>
      <div class="contact-line">
        <svg viewBox="0 0 24 24"><circle cx="12" cy="12" r="10" fill="#fff"/></svg>
        bayhavengrins.com
      </div>
    </div>

    <p class="front-tagline">Creating "Talvering" smiles for Children &amp; Adults</p>
  </section>

  <!-- Back side -->
  <section class="card card-back" aria-label="Business card back">
    <div class="scene-art" role="img" aria-label="Illustrated tropical beach island with palm trees, rocks and sea, with a hand-drawn street map to the office"></div>

    <h2 class="appointment-title">SEE YOU AT YOUR NEXT APPOINTMENT!</h2>
    <div class="field field-for">For<span class="field-line"></span></div>
    <div class="field field-date">Date<span class="field-line"></span></div>
    <div class="field field-time">Time<span class="field-line"></span></div>

    <div class="specialty-band">Specialist in Orthodontic &amp; Maxillofacial Orthopedics</div>
  </section>

</main>
</body>
</html>
```